Restorative Fitness & Nutrition eBook

This is a simple nutrition ebook called Kindlewave. Designed to be download by athletes and fitness enthusiasts who want to improve their athletic performance and recovery after workouts.

This is one of 7 x e-book drafts ready to be designed up.

3 of them (including Kindlewave) are only 3-4 pages long, the other 4 ebooks are much longer and more comprehensive (15-40pages).

I am a restorative health and fitness coach based in Sydney. I work closely with athletes (runners and triathletes) to improve flexibility, core strength, breathing and mindset. I incorporate practices such as yoga, pilates, self-myofascial release, nutrition and meditation.

The ebooks will be available for purchase online and used for home study or training by my clients. They will have instructional photos and copy.

Target Market(s)

Everyday athletes. Runners. Triathletes. Swimmers. Fitness enthusiasts. Health conscious individuals. Aged between 30-50. A mix of male and female, but mostly women.

Industry/Entity Type

Fitness

Font styles to use
Sans Serif
Other font styles liked:
• Freeland Font

Requirements
Must have
• - Be visually beautiful using imagery supplied. I have more if needed.
• - The copy included
• - My logo
• - Short and sweet style. No more than 5 pages. Ideally 3-4
• - Light, white and fresh look
• - Clear and easy to read
Should not have
• Dark black themes
• Squishy text and no white space.

```html
<!DOCTYPE html>
<html lang="en">
<head>
<meta charset="utf-8">
<title>Kindlewave – 7-Days on My Plate</title>
<link href="https://fonts.googleapis.com/css2?family=Arimo:wght@400;700&family=Tinos&display=swap" rel="stylesheet">
<style>
  :root {
    --backdrop: #e6e6e4;
    --page-light: #fdfcf9;
    --heading-coral: #ec6a50;
    --meal-name: #d9573f;
    --text-dark: #3a3a3a;
    --label-dark: #2b2b2b;
    --rule-red: #d6384a;
    --coral: #ef6e55;
    --ink-grey: #5a5a5a;
  }
  * { margin: 0; padding: 0; box-sizing: border-box; }
  html, body { width: 1200px; height: 1200px; overflow: hidden; }
  body {
    background: var(--backdrop);
    position: relative;
    font-family: "Arimo", Arial, sans-serif;
  }
  .page {
    position: absolute;
    width: 353px;
    height: 498px;
    overflow: hidden;
    background: var(--page-light);
    box-shadow: 0 2px 10px rgba(0,0,0,0.12);
  }
  .page--cover { left: 202px; top: 83px; }
  .page--monday { left: 646px; top: 84px; }
  .page--tuesday { left: 202px; top: 619px; }
  .page--wednesday { left: 646px; top: 619px; }

  .cover-photo {
    position: absolute; inset: 0;
    background: linear-gradient(180deg, #fbfbfb 0%, #f4f2ee 40%, #e9ddc8 60%, #cdbfae 100%);
  }
  .cover-photo::after {
    content: ""; position: absolute; left: 0; right: 0; top: 0; height: 56%;
    background: linear-gradient(90deg, rgba(255,255,255,0) 60%, rgba(220,190,110,0.35) 100%);
  }
  .cover-title {
    position: absolute; left: 13px; top: 99px; width: 226px;
    font-family: "Tinos", "Times New Roman", serif;
    color: var(--coral);
  }
  .cover-title__name { font-size: 33px; line-height: 1; font-weight: 400; }
  .cover-title__sub { font-size: 22px; line-height: 1.05; margin-top: 3px; }
  .cover-title__tagline { font-size: 8px; color: var(--ink-grey); margin-top: 3px; white-space: nowrap; }

  .page-backdrop { position: absolute; inset: 0; }
  .page--monday .page-backdrop {
    background: radial-gradient(ellipse 70% 45% at 60% 60%, #f3e9dc 0%, #faf6f0 60%, var(--page-light) 100%);
  }
  .page--tuesday .page-backdrop {
    background: radial-gradient(circle 160px at 45% 50%, #f5e6e6 0%, #fbf6f5 60%, var(--page-light) 100%);
  }
  .page--wednesday .page-backdrop {
    background: radial-gradient(ellipse 60% 40% at 55% 45%, #e6efdc 0%, #f6f9f1 60%, var(--page-light) 100%);
  }

  .day-title {
    position: absolute; left: 0; right: 0; top: 25px;
    text-align: center;
    color: var(--heading-coral);
    font-size: 23px; font-weight: 400; letter-spacing: 0.3px;
  }
  .meal {
    position: absolute; left: 16px; right: 14px;
    color: var(--text-dark);
  }
  .meal__label {
    font-size: 12px; font-weight: 400; line-height: 14px;
    display: block; width: 101px;
    color: var(--label-dark);
    border-bottom: 1px solid var(--rule-red);
    padding-bottom: 2px;
  }
  .meal__name {
    margin-top: 5px;
    font-size: 10.6px; font-weight: 700; color: var(--meal-name);
  }
  .meal__recipe {
    margin-top: 6px;
    font-size: 10.4px; line-height: 12.8px;
    text-align: justify;
  }
</style>
</head>
<body>

<section class="page page--cover">
  <div class="cover-photo" role="img" aria-label="Photo of a smiling woman in a light top and denim shorts holding a jar of oats on a sunny seaside boardwalk"></div>
  <div class="cover-title">
    <h1 class="cover-title__name">KINDLEWAVE</h1>
    <p class="cover-title__sub">7-DAYS ON MY PLATE</p>
    <p class="cover-title__tagline">Nourishing recipes to feed your tired and hungry muscles.</p>
  </div>
</section>

<section class="page page--monday">
  <div class="page-backdrop" role="img" aria-label="Soft faded photo of roasted vegetables in a pan"></div>
  <h2 class="day-title">MONDAY</h2>
  <div class="meal" style="top:77px">
    <span class="meal__label">BREAKFAST</span>
    <h3 class="meal__name">POWER PROTEIN SMOOTHIE</h3>
    <p class="meal__recipe">I blend up 1 serving of protein powder, ½ tsp. of ground cinnamon, 1 tbsp. of chia seeds, ½ cup frozen berries, ½ frozen banana, ½ cup spinach leaves and 1 cup of nut or coconut milk.</p>
  </div>
  <div class="meal" style="top:182px">
    <span class="meal__label">LUNCH</span>
    <h3 class="meal__name">SUPERFOOD BOWL</h3>
    <p class="meal__recipe">I chop and roast sweet potato and eggplant; steam shredded kale and chopped broccoli; and mix chopped coriander and mint through cooked quinoa. Add all cooked ingredients to a bowl, drizzle with tahini, top with chopped almonds and a tbsp. of sauerkraut. It’s a big dose of vitamins, protein and gut lovin goodness.</p>
  </div>
  <div class="meal" style="top:328px">
    <span class="meal__label">DINNER</span>
    <h3 class="meal__name">SOBA NOODLE SPECIAL</h3>
    <p class="meal__recipe">I steam snow peas and frozen green edamame, spiralise a fresh carrot, and mix it all through cooked buckwheat soba noodles. I make a yummy Asian dressing by mixing ¼ cup tamari, 1 tbsp peanut butter, 1 tsp ginger, 1 tsp seasame oil, and the juice of a lime, and then I stir it through the noodles and veg and season with chopped coriander and toasted sesame seeds. Add some cooked tempeh or wild caught grilled salmon for extra protein.</p>
  </div>
</section>

<section class="page page--tuesday">
  <div class="page-backdrop" role="img" aria-label="Soft faded photo of a bowl of dried fruit and flower petals"></div>
  <h2 class="day-title">TUESDAY</h2>
  <div class="meal" style="top:77px">
    <span class="meal__label">BREAKFAST</span>
    <h3 class="meal__name">OVERNIGHT OATS</h3>
    <p class="meal__recipe">The night before I blend 1 banana with 1 tbsp. chia seeds, 1tsp. cinnamon, 1 serving of protein powder, ½ tbsp. of cacao powder and 1 cup of nut milk or water. Then I pour it in a jar and stir through ½ cup of oats. After letting it soak overnight, I enjoy it after my morning run.</p>
  </div>
  <div class="meal" style="top:210px">
    <span class="meal__label">LUNCH</span>
    <h3 class="meal__name">FALAFEL WRAP</h3>
    <p class="meal__recipe">I spread beetroot and hummus dip on a Lebanese bread wrap, and then I fill it with lots of salad goodness (spinach, tomato, cucumber, sauerkraut, pickles, grated carrot) and 2-3 warm falafel balls. Wrap, eat and enjoy!</p>
  </div>
  <div class="meal" style="top:335px">
    <span class="meal__label">DINNER</span>
    <h3 class="meal__name">MEXICAN BOWL</h3>
    <p class="meal__recipe">I cook brown rice and my red kidney bean chili (1-can red kidney beans, ½ diced brown onion, 1 tsp. garlic, 1 grated zucchini, 1 grated carrot, 1 can of diced tomatoes, ½ tsp. chili powder). I fill a bowl with a serving of cooked brown rice, kidney bean chili, a handful of spinach leaves, chopped coriander and a huge dollop of my famous guacamole!</p>
  </div>
</section>

<section class="page page--wednesday">
  <div class="page-backdrop" role="img" aria-label="Soft faded photo of fresh green beans in a colander"></div>
  <h2 class="day-title">WEDNESDAY</h2>
  <div class="meal" style="top:77px">
    <span class="meal__label">BREAKFAST</span>
    <h3 class="meal__name">TOAST AND BANANA</h3>
    <p class="meal__recipe">I toast some soughdough bread and top it with with peanut or almond butter and sliced banana. Easy peasy!</p>
  </div>
  <div class="meal" style="top:170px">
    <span class="meal__label">LUNCH</span>
    <h3 class="meal__name">SALAD AND MIXED BEAN WRAP</h3>
    <p class="meal__recipe">I spread beetroot and hummus dip on a Lebanese bread wrap, and then I fill it with lots of salad goodness (spinach, tomato, cucumber, sauerkraut, pickles, grated carrot) and any leftover beans I may have (the four-bean mix is great!).</p>
  </div>
  <div class="meal" style="top:294px">
    <span class="meal__label">DINNER</span>
    <h3 class="meal__name">ROAST VEGGIE RED CURRY WITH QUINOA</h3>
    <p class="meal__recipe">I chop and roast sweet potato and sliced red capsicum, then I steam green peas and broccoli florets. I gently fry 2 tbsp. of red curry paste with 1 can of coconut milk then I add all the cooked veggies and let it simmer for 10-mins. Spoon it over cooked quinoa and garnish with chopped coriander.</p>
  </div>
</section>

</body>
</html>
```